ZEPRILO.COM is a premium domain sales company. Our competitors are companies like vastplots.example, getparcels.example, peerwords.example. Our current site is at www.zeprilos.example.

We want to have the ability to search for domains, to highlight special offers and have some testimonials on the index page.

The logo for the site is attached.

Please be sure that the order form fits on the screen without scrolling the page. I want the entire form, including the submit button to fit without any page scrolling.

Delivered product - INDEX PAGE, ORDER FORM AND CONTENT PAGE PSDs.

Target Market(s)

Small to Medium business professionals

Industry/Entity Type

It Company

Requirements
Must have
• 1. List of domains for sale
2. Simple search box with button to run the search
3. link for advanced search
4. testimonial area. Note - this can be a small box where a different testimonial is displayed on each page load.
Nice to have
• Would like the site to have some white space. Don't want a heavily packed website. Give it an "airy" feel.

```html
<!DOCTYPE html>
<html lang="en">
<head>
<meta charset="utf-8">
<title>ZEPRILO.COM – Premium Domains</title>
<link rel="stylesheet" href="https://fonts.googleapis.com/css2?family=Open+Sans:ital,wght@0,300;0,400;0,600;0,700;1,400&display=swap">
<style>
:root{
  --blue:#1a5fa8;--blue-dark:#0d4a8c;--green:#0b7a3b;--orange:#d4821b;--red:#d9403a;
  --text:#444;--muted:#777;--line:#d6e0e4;--page:#f2f7f8;--footer:#2e2e2e;--white:#fff;
}
*{box-sizing:border-box;margin:0;padding:0}
html,body{width:670px;height:1200px;overflow:hidden}
body{font-family:"Open Sans",Arial,sans-serif;background:var(--page);color:var(--text);position:relative}
.site-header{height:62px;background:#f8f8f8;position:relative}
.brand{position:absolute;left:56px;top:20px;font-size:21px;font-weight:700;color:var(--blue);letter-spacing:.3px}
.helpline{position:absolute;right:56px;top:13px;text-align:right;color:#555}
.helpline p{font-size:11.5px}
.helpline .phone{font-size:17px;font-weight:300;display:flex;align-items:center;gap:5px;justify-content:flex-end}
.hero{position:relative;height:288px;overflow:hidden}
.hero-photo{position:absolute;inset:0;background:linear-gradient(90deg,#2a2420 0%,#6a5a48 30%,#c9b48e 55%,#e8dcc0 75%,#a89478 100%)}
.hero-photo::after{content:"";position:absolute;inset:0;background:linear-gradient(180deg,rgba(255,255,255,.15) 0%,rgba(0,0,0,0) 55%,rgba(0,0,0,.55) 100%)}
.hero-content{position:absolute;left:286px;top:28px;width:330px}
.hero-title{font-size:27px;font-weight:400;color:var(--blue);line-height:1.07}
.search-form{display:flex;margin-top:10px;height:39px}
.search-input{flex:1;border:1px solid #ccc;background:#fff;font:italic 11.5px "Open Sans",sans-serif;color:#999;padding:0 9px;display:flex;align-items:center}
.search-button{width:69px;background:var(--blue-dark);color:#fff;font-size:11px;display:flex;align-items:center;justify-content:center;gap:4px;border:1px solid #0a3a70}
.advanced-link{display:flex;align-items:center;gap:4px;margin-top:9px;font-size:9px;color:#333;text-decoration:underline}
.about{position:absolute;left:56px;top:362px;width:558px}
.about h1{font-size:19px;font-weight:400;color:var(--blue)}
.about h1 small{font-size:12px}
.about p{font-size:7.6px;line-height:1.55;color:#555;margin-top:8px}
.domains{position:absolute;left:56px;top:494px;width:558px;height:238px;background:#fff;border:1px solid var(--line)}
.tabs{display:flex;height:26px;border-bottom:1px solid var(--line)}
.tab{flex:1;display:flex;align-items:center;justify-content:center;font-size:12px;color:#222;border-left:1px solid var(--line)}
.tab:first-child{border-left:0}
.tab.active{background:var(--green);color:#fff}
.domain-table{width:100%;border-collapse:collapse;font-size:7.6px}
.domain-table th{font-size:10px;font-weight:600;color:var(--blue);text-align:left;height:24px;background:#f6f8f9;border-bottom:1px solid #e6ecee}
.domain-table td{height:23.5px;border-bottom:1px solid #eef2f3}
.domain-table tr:last-child td{border-bottom:0}
.domain-table th:first-child,.domain-table td:first-child{padding-left:11px;width:205px}
.domain-table .price{width:127px}
.domain-table .cat{width:128px}
.domain-name{font-weight:600}
.row-green td{color:var(--green)}
.row-orange td{color:var(--orange)}
.add-btn{display:inline-flex;align-items:center;gap:5px;color:#fff;font-size:6.3px;font-weight:600;padding:3px 7px;border-radius:2px;margin-left:5px}
.row-green .add-btn{background:var(--green)}
.row-orange .add-btn{background:var(--orange)}
.section-title{position:absolute;left:56px;width:558px;height:33px;background:#f8fbfb;border:1px solid var(--line);display:flex;align-items:center;justify-content:center;font-size:13.5px;font-weight:600;color:#333}
.section-title::after{content:"";position:absolute;bottom:-6px;left:50%;margin-left:-6px;width:11px;height:11px;background:#f8fbfb;border-right:1px solid var(--line);border-bottom:1px solid var(--line);transform:rotate(45deg)}
.why{top:756px}
.features{position:absolute;left:56px;top:800px;width:558px;display:grid;grid-template-columns:1fr 1fr;column-gap:36px}
.feature{height:66px;padding-top:2px}
.feature:nth-child(-n+2){border-bottom:1px solid #e1e8ea}
.feature:nth-child(n+3){padding-top:10px}
.feature h3{display:flex;align-items:center;gap:5px;font-size:11px;font-weight:400}
.feature p{font-size:7px;line-height:1.6;color:#777;margin:5px 0 0 22px;font-weight:300}
.c-blue{color:var(--blue)}.c-red{color:var(--red)}.c-orange{color:var(--orange)}.c-green{color:var(--green)}
.happy{top:942px}
.testimonial{position:absolute;left:56px;top:980px;width:558px;height:74px;background:#fff;padding:10px 22px 0 22px}
.testimonial p{font-size:7.7px;font-style:italic;line-height:1.9;color:#555}
.quote{position:absolute;color:var(--red);font:700 18px Georgia,serif}
.quote.open{left:9px;top:-3px}.quote.close{right:8px;bottom:-8px}
.site-footer{position:absolute;left:0;top:1068px;width:670px;height:132px;background:var(--footer);color:#ddd}
.footer-col{position:absolute;top:15px}
.footer-col h4{font-size:10px;font-weight:400;color:#fff;margin-bottom:6px}
.footer-col li{list-style:none;font-size:6.6px;line-height:1.55;color:#ccc}
.footer-contact{position:absolute;right:56px;top:34px;text-align:right;font-size:10px;font-weight:300;line-height:1.4;color:#eee}
.social{display:flex;gap:6px;justify-content:flex-end;margin-top:4px}
.social span{width:14px;height:14px;display:block}
.copyright{position:absolute;left:0;right:0;top:111px;text-align:center;font-size:6.6px;color:#bbb}
</style>
</head>
<body>
<header class="site-header">
  <div class="brand">ZEPRILO.COM</div>
  <div class="helpline">
    <p>Questions? We’re here to help!</p>
    <p class="phone"><svg width="9" height="12" viewBox="0 0 9 12"><rect x="0.5" y="0.5" width="8" height="11" rx="1.5" fill="#1a5fa8"/><rect x="2" y="2" width="5" height="3" fill="#fff"/><rect x="2" y="6.5" width="5" height="3.5" fill="#9cc"/></svg>1480.336.902</p>
  </div>
</header>

<section class="hero">
  <div class="hero-photo" role="img" aria-label="Businesswoman with sunglasses sitting on a car bonnet, working on a laptop in a bright city setting"></div>
  <div class="hero-content">
    <h2 class="hero-title">Find the best name for your business...</h2>
    <div class="search-form">
      <div class="search-input">Enter Domain Name...</div>
      <div class="search-button"><svg width="10" height="10" viewBox="0 0 10 10"><circle cx="4" cy="4" r="3" fill="none" stroke="#fff" stroke-width="1.6"/><line x1="6.2" y1="6.2" x2="9" y2="9" stroke="#fff" stroke-width="1.8"/></svg>SEARCH</div>
    </div>
    <div class="advanced-link"><svg width="8" height="8" viewBox="0 0 10 10"><circle cx="4" cy="4" r="3" fill="none" stroke="#333" stroke-width="1.4"/><line x1="6.2" y1="6.2" x2="9" y2="9" stroke="#333" stroke-width="1.6"/></svg>Advanced Search</div>
  </div>
</section>

<section class="about">
  <h1>About ZEPRILO<small>.com</small></h1>
  <p>Le Lorem Ipsum est simplement du faux texte employé dans la composition et la mise en page avant impression. Le Lorem Ipsum est le faux texte standard de l'imprimerie depuis les années 1500, quand un peintre anonyme assembla ensemble des morceaux de texte pour réaliser un livre spécimen de polices de texte.</p>
  <p>Il n'a pas fait que survivre cinq siècles, mais s'est aussi adapté à la bureautique informatique, sans que son contenu n'en soit modifié. Il a été popularisé dans les années 1960.</p>
</section>

<section class="domains">
  <div class="tabs">
    <div class="tab active">Featured Domains</div>
    <div class="tab">Domain Categories</div>
    <div class="tab">Daily Domain Deals</div>
  </div>
  <table class="domain-table">
    <thead><tr><th>Description</th><th class="price">Price</th><th class="cat">Category</th><th>Add</th></tr></thead>
    <tbody>
      <tr class="row-green"><td class="domain-name">GlowBoards.example</td><td>$9,400</td><td>Contracts</td><td><span class="add-btn">Add to Cart <b>+</b></span></td></tr>
      <tr class="row-orange"><td class="domain-name">JobHarbor.example</td><td>$5,990</td><td>Careers</td><td><span class="add-btn">Add to Cart <b>+</b></span></td></tr>
      <tr class="row-green"><td class="domain-name">NoteMarker.example</td><td>$7,995</td><td>Maps</td><td><span class="add-btn">Add to Cart <b>+</b></span></td></tr>
      <tr class="row-orange"><td class="domain-name">RelevantMarkets.example</td><td>$5,790</td><td>E-Commerce</td><td><span class="add-btn">Add to Cart <b>+</b></span></td></tr>
      <tr class="row-green"><td class="domain-name">HeartBeacon.example</td><td>$6,395</td><td>Rock and Pop</td><td><span class="add-btn">Add to Cart <b>+</b></span></td></tr>
      <tr class="row-orange"><td class="domain-name">NailAndPolishKits.example</td><td>$5,495</td><td>Furniture</td><td><span class="add-btn">Add to Cart <b>+</b></span></td></tr>
      <tr class="row-green"><td class="domain-name">LocalStyleRoom.example</td><td>$5,390</td><td>Candy</td><td><span class="add-btn">Add to Cart <b>+</b></span></td></tr>
      <tr class="row-orange"><td class="domain-name">KeenShowcase.example</td><td>$5,390</td><td>Glossary</td><td><span class="add-btn">Add to Cart <b>+</b></span></td></tr>
    </tbody>
  </table>
</section>

<h2 class="section-title why">Why Choose ZEPRILO.com?</h2>
<section class="features">
  <div class="feature">
    <h3 class="c-blue"><svg width="16" height="16" viewBox="0 0 16 16"><circle cx="8" cy="8" r="7" fill="#1a5fa8"/><circle cx="8" cy="8" r="3" fill="#fff"/><g stroke="#fff" stroke-width="2"><line x1="8" y1="1" x2="8" y2="4"/><line x1="8" y1="12" x2="8" y2="15"/><line x1="1" y1="8" x2="4" y2="8"/><line x1="12" y1="8" x2="15" y2="8"/></g></svg>24 / 7 Professional Support</h3>
    <p>On sait depuis longtemps que travailler avec du texte lisible et contenant du sens est source de distractions.</p>
  </div>
  <div class="feature">
    <h3 class="c-red"><svg width="16" height="16" viewBox="0 0 16 16"><path d="M8 8V1A7 7 0 1 1 1 8Z" fill="#d9403a"/><path d="M9 7V0.5A6.5 6.5 0 0 1 15.5 7Z" fill="#d9403a"/></svg>100% Network and Uptime</h3>
    <p>On sait depuis longtemps que travailler avec du texte lisible et contenant du sens est source de distractions.</p>
  </div>
  <div class="feature">
    <h3 class="c-orange"><svg width="16" height="16" viewBox="0 0 16 16"><g fill="none" stroke="#d4821b" stroke-width="2.2"><path d="M13.5 6A6 6 0 0 0 2.8 5"/><path d="M2.5 10A6 6 0 0 0 13.2 11"/></g><path d="M1 2v5h5z" fill="#d4821b"/><path d="M15 14V9h-5z" fill="#d4821b"/></svg>100% Network and Uptime</h3>
    <p>On sait depuis longtemps que travailler avec du texte lisible et contenant du sens est source de distractions.</p>
  </div>
  <div class="feature">
    <h3 class="c-green"><svg width="16" height="16" viewBox="0 0 16 16"><circle cx="8" cy="8" r="6.5" fill="none" stroke="#0b7a3b" stroke-width="2"/><path d="M8 4v4.5h3" fill="none" stroke="#0b7a3b" stroke-width="1.8"/></svg>24 / 7 Professional Support</h3>
    <p>On sait depuis longtemps que travailler avec du texte lisible et contenant du sens est source de distractions.</p>
  </div>
</section>

<h2 class="section-title happy">Happy Customers</h2>
<blockquote class="testimonial">
  <span class="quote open">“</span>
  <p>Le Lorem Ipsum est simplement du faux texte employé dans la composition et la mise en page avant impression. Le Lorem Ipsum est le faux texte standard de l'imprimerie depuis les années 1500, quand un peintre anonyme assembla ensemble des morceaux de texte pour réaliser un livre spécimen de polices de texte.</p>
  <span class="quote close">”</span>
</blockquote>

<footer class="site-footer">
  <div class="footer-col" style="left:56px"><h4>DOMAINS</h4><ul><li>Categories</li><li>Sell Your Domains</li></ul></div>
  <div class="footer-col" style="left:176px"><h4>DOMAINS</h4><ul><li>Plusieurs</li><li>structures</li><li>phrases</li><li>touches</li><li>aléatoires</li></ul></div>
  <div class="footer-col" style="left:286px"><h4>COMPANY</h4><ul><li>About</li><li>Contact</li><li>Policies</li></ul></div>
  <div class="footer-col" style="left:382px"><h4>SUITES</h4><ul><li>Contrairement</li><li>répandue</li><li>intéressé</li><li>étudiant</li><li>incontestable</li></ul></div>
  <div class="footer-contact">
    <p>Call our domain Expert today</p>
    <p>6120.447.318 Or +1 3908 712 564</p>
    <div class="social"><span style="background:#2a56a0"></span><span style="background:#1e6fa8"></span><span style="background:#3aa5e0"></span></div>
  </div>
  <p class="copyright">© Copyrights 2013 All rights Reserved</p>
</footer>
</body>
</html>
```